High end Sports Bar/ Restaurant Postcard Design

We are a high end sports bar/restaurant in forest hills on Benning street, we have high quality bar food, 24 draft beers, wine on tap and a great selection of whiskeys & scotches.
What we need is a brightly colored postcard that advertises our weekly events. It must be easy to read but eye-catching and full of fun images that will want to make people come in and drink & eat!
We are called Harlow Commons and have a gastropub feel with one entire wall covered in brick but with 9 t.v's all with audio for all sports games. We are definitely a restaurant too so its not all about sports however we will be carrying the GBX & Coastal Victory League Soccer packages.
On the back of the card we would like to advertise our lunch menu is Monday to Friday 10a.m - 3p.m. Dinner is Sunday - Monday 3p.m - 11p.m and Brunch on Saturday & Sunday. Late night bar menu also available Thursday, Friday & Saturday from 11p.m - 1a.m
Address: 54-16 Benning Street, Forest Hills, N.Y 11382 Phone number: 718 555.0143

Reason: We are extending the deadline to give us time to figure out which design is best for us, thank you all for your participation

Target Market(s)

21 - 45 year olds

Industry/Entity Type

Restaurant

Requirements
Must have
• Each individual days event must be eye-catching yet easy to read.

```html
<!DOCTYPE html>
<html lang="en">
<head>
<meta charset="utf-8">
<title>Harlow Commons – Weekly Events</title>
<link href="https://fonts.googleapis.com/css2?family=Bevan&family=Oswald:wght@500;700&family=Allura&family=Raleway:wght@400&family=Poiret+One&family=Lobster&family=Comfortaa:wght@400;600&family=Quicksand:wght@500;600&family=Fredoka:wght@600&family=Short+Stack&display=swap" rel="stylesheet">
<style>
  :root {
    --brick: #b3221f;
    --brick-dark: #7e1512;
    --sign-top: #3a3a3a;
    --sign-bottom: #0d0d0d;
    --white: #ffffff;
    --monday: #3ea63a;
    --tuesday-top: #3d47a8;
    --tuesday-bottom: #5f6ad1;
    --wednesday: #f47a1f;
    --thursday: #b24aa7;
    --weekend: #7b3596;
    --sunday-top: #2b7f8c;
    --sunday-bottom: #47c7cf;
    --band: #b6c73a;
    --band-ink: #2f3a12;
    --ink-dark: #222;
  }
  * { margin: 0; padding: 0; box-sizing: border-box; }
  html, body { width: 1200px; height: 930px; overflow: hidden; }
  body { position: relative; background: var(--brick); }

  .wall { position: absolute; inset: 0; background: radial-gradient(ellipse at center, var(--brick) 0%, var(--brick-dark) 100%); }

  .sign {
    position: absolute; left: 27px; top: 27px; width: 1146px; height: 165px;
    background: linear-gradient(var(--sign-top), var(--sign-bottom));
    box-shadow: 0 4px 10px rgba(0,0,0,.5);
  }
  .sign-frame {
    position: absolute; left: 40px; top: 28px; width: 1066px; height: 96px;
    border: 2px solid #d8d8d8;
    display: flex; align-items: center; justify-content: center;
  }
  .sign-name {
    font-family: "Bevan", serif; font-size: 72px; letter-spacing: 5px;
    color: #e8e8e8; text-transform: uppercase; line-height: 1;
  }

  .card {
    position: absolute; width: 357px; height: 234px; color: var(--white);
    box-shadow: 3px 4px 8px rgba(0,0,0,.45); overflow: hidden;
  }
  .col1 { left: 40px; } .col2 { left: 417px; } .col3 { left: 796px; }
  .row1 { top: 231px; } .row2 { top: 483px; }

  /* Monday */
  .monday { background: var(--monday); }
  .monday .day { position: absolute; left: 10px; top: 14px; font: 700 54px/1 "Oswald", sans-serif; }
  .monday .deal { position: absolute; left: 10px; top: 76px; font: 700 21px/1.05 "Oswald", sans-serif; }
  .monday .price { position: absolute; left: 210px; top: 14px; font: 700 100px/1 "Oswald", sans-serif; letter-spacing: -3px; }
  .monday .notes { position: absolute; left: 12px; top: 144px; font: 400 16px/1.35 "Raleway", sans-serif; }

  /* Tuesday */
  .tuesday { background: linear-gradient(var(--tuesday-top), var(--tuesday-bottom)); text-align: center; }
  .tuesday .day { position: absolute; left: 0; right: 0; top: 18px; font: 400 86px/1 "Allura", cursive; }
  .tuesday .title { position: absolute; left: 0; right: 0; top: 104px; font: 400 32px/1 "Raleway", sans-serif; }
  .tuesday .when {
    position: absolute; left: 0; right: 0; top: 154px;
    font: 400 54px/1 "Poiret One", sans-serif; white-space: nowrap;
    transform: scaleX(.74); transform-origin: center;
  }
  .tuesday .when .amp { font-family: "Allura", cursive; font-size: 64px; }

  /* Wednesday */
  .wednesday { background: var(--wednesday); }
  .wednesday .day { position: absolute; left: 14px; top: 14px; font: 700 50px/1 "Oswald", sans-serif; letter-spacing: -1px; }
  .wednesday .event { position: absolute; left: 14px; top: 78px; font: 700 32px/1 "Oswald", sans-serif; }
  .wednesday .hour { position: absolute; left: 298px; top: 6px; font: 700 66px/1 "Oswald", sans-serif; }
  .wednesday .pm { position: absolute; left: 298px; top: 84px; font: 700 26px/1 "Oswald", sans-serif; }
  .wednesday .blurb { position: absolute; left: 14px; right: 10px; top: 148px; font: 500 22px/1.25 "Quicksand", sans-serif; color: var(--ink-dark); text-align: center; }

  /* Thursday */
  .thursday { background: var(--thursday); }
  .thursday .day { position: absolute; left: 22px; top: 6px; font: 400 86px/1 "Allura", cursive; }
  .thursday .event { position: absolute; left: 26px; top: 86px; font: 400 36px/1 "Lobster", cursive; }
  .thursday .hours { position: absolute; left: 14px; top: 150px; font: 400 46px/1 "Allura", cursive; }
  .thursday .deal { position: absolute; right: 18px; top: 142px; font: 400 22px/1.2 "Raleway", sans-serif; text-align: right; }

  /* Friday & Saturday */
  .weekend { background: var(--weekend); }
  .weekend .days { position: absolute; left: 18px; top: 8px; font: 400 50px/1.02 "Comfortaa", sans-serif; }
  .weekend .event { position: absolute; left: 18px; top: 126px; font: 600 31px/1 "Comfortaa", sans-serif; }
  .weekend .blurb { position: absolute; left: 0; right: 0; top: 172px; font: 400 22px/1.2 "Raleway", sans-serif; text-align: center; }

  /* Sunday */
  .sunday { background: linear-gradient(var(--sunday-top), var(--sunday-bottom)); text-align: center; }
  .sunday .day { position: absolute; left: 0; right: 0; top: 14px; font: 500 74px/1 "Quicksand", sans-serif; letter-spacing: 2px; }
  .sunday .hour { position: absolute; left: 0; right: 0; top: 92px; font: 400 50px/1 "Poiret One", sans-serif; }
  .sunday .event { position: absolute; left: 0; right: 0; top: 140px; font: 500 66px/1 "Quicksand", sans-serif; }

  /* Happy hour band */
  .band {
    position: absolute; left: 45px; top: 738px; width: 1115px; height: 150px;
    background: var(--band); box-shadow: 3px 4px 8px rgba(0,0,0,.45);
  }
  .band .days {
    position: absolute; left: 18px; top: 18px; font: 600 54px/1.02 "Fredoka", sans-serif;
    color: var(--white); -webkit-text-stroke: 2px var(--band-ink);
  }
  .band .title { position: absolute; left: 282px; top: 22px; font: 500 60px/1 "Quicksand", sans-serif; color: var(--white); }
  .band .hours { position: absolute; left: 284px; top: 88px; font: 500 44px/1 "Quicksand", sans-serif; color: var(--white); }
  .band .specials { position: absolute; right: 22px; top: 52px; font: 400 24px/1.4 "Short Stack", cursive; color: var(--white); text-align: right; }
</style>
</head>
<body>
  <div class="wall" role="img" aria-label="Red brick wall background"></div>

  <header class="sign">
    <div class="sign-frame"><h1 class="sign-name">Harlow Commons</h1></div>
  </header>

  <section class="card monday col1 row1">
    <div class="day">Monday</div>
    <div class="deal">Burger &amp; Beer<br>or Salad &amp; Wine</div>
    <div class="price">$10</div>
    <div class="notes">*choice of HC Burger, Garden Burger<br>&nbsp;or HC Chx Sandwich, Any Salad<br>* Chicken or Steak are additional</div>
  </section>

  <section class="card tuesday col2 row1">
    <div class="day">Tuesday</div>
    <div class="title">Happy Hour</div>
    <div class="when">ALL DAY<span class="amp">&amp;</span>NIGHT</div>
  </section>

  <section class="card wednesday col3 row1">
    <div class="day">Wednesday</div>
    <div class="event">Trivia Night</div>
    <div class="hour">8</div>
    <div class="pm">p.m</div>
    <div class="blurb">Come test your knowledge of irrelevant facts &amp; win a prize!</div>
  </section>

  <section class="card thursday col1 row2">
    <div class="day">Thursday</div>
    <div class="event">Ladies Night</div>
    <div class="hours">8p.m-close</div>
    <div class="deal">Ladies drink<br>½ price<br>ALL NIGHT</div>
  </section>

  <section class="card weekend col2 row2">
    <div class="days">Friday &amp;<br>Saturday</div>
    <div class="event">live entertainment</div>
    <div class="blurb">Food &amp; Drink Specials<br>Every weekend</div>
  </section>

  <section class="card sunday col3 row2">
    <div class="day">SUNday</div>
    <div class="hour">9 p.m</div>
    <div class="event">karaoke</div>
  </section>

  <section class="band">
    <div class="days">Monday<br>– Friday</div>
    <div class="title">HAPPY HOUR</div>
    <div class="hours">11a.m – 8p.m</div>
    <div class="specials">10 select draft beers...$4 each<br>$1 off all bottles...$4 select wine</div>
  </section>
</body>
</html>
```